Help redesign our website

After succesfully recieveing a round of seed funding we are looking for someone to help re-design our website.
We did initially get a design created but after much debate with the team members we feel like it does have a slighly outdated feel to it and would much prefer something that will last for many years to come.
I will attach the current home and innerpage designs for you to take a look at. You will be redesigning these.
When you see the current design you will see that while it's not *bad* its maybe now how website are now feeling. It's not modern.
I will be commenting and giving feedback on all designs so ask all the questions you want.

```html
<!DOCTYPE html>
<html lang="en">
<head>
<meta charset="utf-8">
<title>CineReel – Night Vector</title>
<link href="https://fonts.googleapis.com/css2?family=Inter:wght@400;500;600;700&display=swap" rel="stylesheet">
<style>
:root{
  --bg:#111317;
  --surface:#1a1d23;
  --surface-2:#22262e;
  --line:#2a2e36;
  --text:#eef0f4;
  --body:#b4bac5;
  --muted:#8d94a1;
  --dim:#666d79;
  --accent:#3b8cff;
  --accent-soft:rgba(59,140,255,.14);
}
*{box-sizing:border-box;margin:0;padding:0}
html,body{width:1200px;height:1000px;overflow:hidden;background:var(--bg)}
body{position:relative;font-family:"Inter",Arial,sans-serif;color:var(--text)}
ul{list-style:none}
.page{width:960px;margin:0 auto}

/* header */
.site-header{border-bottom:1px solid var(--line)}
.topbar{height:56px;display:flex;align-items:center;justify-content:space-between}
.brand{display:flex;align-items:center;gap:10px;font-size:20px;font-weight:700;letter-spacing:1.5px;color:var(--text)}
.brand-mark{width:14px;height:14px;border-radius:3px;background:var(--accent)}
.util-links{display:flex;gap:22px;font-size:12px;color:var(--muted)}
.util-links .is-active{color:var(--text)}
.nav-row{height:52px;display:flex;align-items:center;border-top:1px solid var(--line)}
.main-nav{display:flex;align-items:center;gap:2px;font-size:13px;font-weight:500;color:var(--body)}
.main-nav a{padding:7px 10px;border-radius:8px;white-space:nowrap}
.main-nav .nav-feature{color:var(--accent)}
.main-nav .is-active{background:var(--surface-2);color:var(--text)}
.nav-divider{width:1px;height:18px;background:var(--line);margin:0 8px}
.search{margin-left:auto;display:flex;align-items:center;gap:8px}
.search-input{width:168px;height:34px;border-radius:8px;background:var(--surface);border:1px solid var(--line);font-size:12px;color:var(--dim);display:flex;align-items:center;gap:8px;padding:0 10px}
.search-btn{height:34px;padding:0 14px;border-radius:8px;background:var(--accent);color:#fff;font-size:12px;font-weight:600;display:flex;align-items:center}
.adv-search{font-size:12px;color:var(--accent);margin-left:6px;white-space:nowrap}

/* layout */
.content{display:grid;grid-template-columns:640px 296px;gap:24px;margin-top:16px}
.col{display:flex;flex-direction:column;gap:16px}
.card{background:var(--surface);border:1px solid var(--line);border-radius:12px;padding:18px 20px}
.card-head{height:24px;display:flex;align-items:center;justify-content:space-between;font-size:14px;font-weight:600;margin-bottom:14px}
.card-head .accent{color:var(--accent);margin-right:6px}
.year-tag{font-size:11px;font-weight:500;color:var(--muted);background:var(--surface-2);padding:3px 9px;border-radius:20px}

/* film detail */
.detail{display:grid;grid-template-columns:140px 1fr;gap:20px}
.poster{width:140px;height:190px;border-radius:8px;background:linear-gradient(165deg,#3b3f46 0%,#1e2025 55%,#5b2f28 100%)}
.poster-meta{height:24px;margin-top:10px;display:flex;align-items:center;justify-content:space-between}
.synopsis{font-size:11px;line-height:15px;color:var(--body)}
.synopsis p{margin-bottom:9px}
.synopsis p:last-child{margin-bottom:0;padding-top:9px;border-top:1px solid var(--line);color:var(--muted)}

/* video */
.video-card{padding:16px 20px}
.player{position:relative;height:190px;border-radius:8px;overflow:hidden}
.player-art{position:absolute;inset:0;background:linear-gradient(180deg,#23302c 0%,#4f4230 48%,#8a4a22 62%,#181c1d 100%)}
.player-bar{position:absolute;left:0;right:0;top:0;height:30px;padding:0 12px;display:flex;align-items:center;gap:16px;font-size:11px;color:#fff;background:linear-gradient(rgba(0,0,0,.7),rgba(0,0,0,0))}
.player-bar .title{flex:1;white-space:nowrap;overflow:hidden;text-overflow:ellipsis}
.player-bar span:not(.title){color:#d7dbe2}
.play-btn{position:absolute;left:50%;top:50%;transform:translate(-50%,-50%)}

/* comments */
.comment-row{display:flex;align-items:center;gap:12px}
.avatar{width:44px;height:44px;border-radius:50%;background:var(--surface-2);flex:none;overflow:hidden}
.comment-field{flex:1;height:48px;border-radius:8px;background:var(--bg);border:1px solid var(--line);font-size:12px;color:var(--dim);display:flex;align-items:center;padding:0 14px}
.submit{height:40px;padding:0 18px;border-radius:8px;background:var(--accent);color:#fff;font-size:12px;font-weight:600;display:flex;align-items:center}
.load-more{margin-top:16px;padding-top:12px;border-top:1px solid var(--line);text-align:center;font-size:12px;color:var(--muted)}

/* sidebar */
.side-card{padding:16px}
.tabs{display:flex;gap:4px;padding:3px;background:var(--bg);border-radius:9px;margin-bottom:12px}
.tab{flex:1;height:28px;border-radius:7px;display:flex;align-items:center;justify-content:center;font-size:12px;font-weight:500;color:var(--muted)}
.tab.is-active{background:var(--surface-2);color:var(--accent)}
.feature{position:relative;height:104px;border-radius:8px;overflow:hidden}
.feature + .feature{margin-top:12px}
.feature-caption{position:absolute;left:0;right:0;bottom:0;height:36px;padding:0 10px;display:flex;align-items:center;justify-content:space-between;font-size:12px;font-weight:500;background:linear-gradient(rgba(0,0,0,0),rgba(0,0,0,.75))}

.film-list li{display:flex;gap:12px;height:60px}
.film-list li + li{margin-top:12px}
.film-thumb{width:52px;height:60px;border-radius:6px;flex:none}
.film-info{flex:1;display:flex;flex-direction:column;justify-content:space-between}
.film-title{font-size:13px;font-weight:600;line-height:16px}
.film-meta{font-size:11px;color:var(--muted);line-height:14px}
.film-link{align-self:flex-start;height:20px;padding:0 10px;border-radius:20px;background:var(--accent-soft);font-size:10.5px;color:var(--body);display:flex;align-items:center;gap:4px}
.film-link b{font-weight:500;color:var(--accent)}

.ad-banner{height:118px;border-radius:8px;background:linear-gradient(100deg,#f4b400 0%,#f5c423 50%,#c9281e 51%,#e4a800 100%)}

/* footer */
.site-footer{position:absolute;left:0;top:930px;width:1200px;height:70px;background:#0c0d10;border-top:1px solid var(--line)}
.footer-inner{height:69px;display:flex;align-items:center;gap:48px}
.link-group h4{font-size:12px;font-weight:600;margin-bottom:5px}
.link-group ul{display:grid;grid-template-columns:auto auto;column-gap:18px;row-gap:2px;font-size:11px;color:var(--dim)}
.company{font-size:13px;font-weight:600;letter-spacing:1px;color:var(--muted)}
.legal{margin-left:auto;text-align:right;font-size:11px;line-height:17px;color:var(--dim)}
</style>
</head>
<body>

<header class="site-header">
  <div class="page topbar">
    <div class="brand"><span class="brand-mark"></span>CINEREEL</div>
    <nav class="util-links"><a class="is-active">About</a><a>Review</a><a>FAQ</a><a>Contacts</a></nav>
  </div>
  <div class="page nav-row">
    <nav class="main-nav">
      <a class="nav-feature">Comming Soon</a>
      <a class="nav-feature">Theaters</a>
      <span class="nav-divider"></span>
      <a class="is-active">Year</a>
      <a>Genre's</a>
      <a>Studio's</a>
      <a>Actors/Actress</a>
    </nav>
    <div class="search">
      <div class="search-input">
        <svg width="13" height="13" viewBox="0 0 13 13" fill="none" stroke="#666d79" stroke-width="1.6"><circle cx="5.5" cy="5.5" r="4.3"/><path d="M8.8 8.8L12 12"/></svg>
        Search Keyword
      </div>
      <a class="search-btn">Search</a>
      <a class="adv-search">Advance Search</a>
    </div>
  </div>
</header>

<main class="page content">
  <div class="col">
    <section class="card">
      <div class="card-head"><span><span class="accent">NIGHT</span>VECTOR</span><span class="year-tag">2013</span></div>
      <div class="detail">
        <div>
          <div class="poster" role="img" aria-label="Film poster for Night Vector"></div>
          <div class="poster-meta">
            <svg width="70" height="12" viewBox="0 0 70 12" fill="#3b8cff">
              <path id="star" d="M6 .5l1.6 3.6 3.9.4-2.9 2.6.9 3.8L6 9 2.5 10.9l.9-3.8L.5 4.5l3.9-.4z"/>
              <use href="#star" x="14"/><use href="#star" x="28"/><use href="#star" x="42"/>
              <use href="#star" x="56" fill="#3a3f48"/>
            </svg>
            <svg width="16" height="16" viewBox="0 0 16 16" fill="#8d94a1" stroke="#8d94a1" stroke-width="1.3">
              <circle cx="12" cy="3.5" r="2"/><circle cx="4" cy="8" r="2"/><circle cx="12" cy="12.5" r="2"/>
              <path d="M12 3.5L4 8l8 4.5" fill="none"/>
            </svg>
          </div>
        </div>
        <div class="synopsis">
          <p>Lorem Ipsum is simply dummy text of the printing and typesetting industry. Lorem Ipsum has been the industry's standard dummy text ever since Lorem Ipsum is simply dummy text of the printing and typesetting industry. Lorem Ipsum has been the industry's standard dummy text ever since</p>
          <p>Lorem Ipsum is simply dummy text of the printing and typesetting industry. Lorem Ipsum has been the industry's standard dummy text ever since Lorem Ipsum is simply dummy text of the printing and typesetting industry. Lorem Ipsum has been the industry's standard dummy text ever since</p>
          <p>Lorem Ipsum is simply dummy text of the printing and typesetting industry. Lorem Ipsum has been the industry's standard dummy text ever since</p>
          <p>Lorem Ipsum is simply dummy text of the printing and typesetting industry. Lorem Ipsum has been the industry's standard dummy text ever since</p>
        </div>
      </div>
    </section>

    <section class="card video-card">
      <div class="card-head"><span class="accent">VIDEO</span></div>
      <div class="player">
        <div class="player-art" role="img" aria-label="Trailer still of a burning stone building at night"></div>
        <div class="player-bar"><span class="title">Night Vector Map Pack Flyover Trailer - Med...</span><span>Share</span><span>More info</span></div>
        <svg class="play-btn" width="52" height="52" viewBox="0 0 52 52"><circle cx="26" cy="26" r="26" fill="rgba(255,255,255,.92)"/><path d="M21 16l16 10-16 10z" fill="#111317"/></svg>
      </div>
    </section>

    <section class="card">
      <div class="card-head">Comments</div>
      <div class="comment-row">
        <div class="avatar">
          <svg width="44" height="44" viewBox="0 0 44 44" fill="#4a505b"><circle cx="22" cy="17" r="7.5"/><path d="M8 44c0-10 6-15 14-15s14 5 14 15z"/></svg>
        </div>
        <div class="comment-field">Write a comment…</div>
        <a class="submit">Submit</a>
      </div>
      <div class="load-more">Load More</div>
    </section>
  </div>

  <aside class="col">
    <section class="card side-card">
      <div class="tabs"><span class="tab is-active">Popular</span><span class="tab">Upcoming</span><span class="tab">On Now!</span></div>
      <div class="feature" role="img" aria-label="Superhero film artwork" style="background:radial-gradient(ellipse at center,#6a1f1f 0%,#2a1a1a 55%,#8e9096 100%)">
        <div class="feature-caption">Title of the Movie
          <svg width="22" height="22" viewBox="0 0 22 22"><circle cx="11" cy="11" r="11" fill="rgba(255,255,255,.92)"/><path d="M9 6.5l6 4.5-6 4.5z" fill="#111317"/></svg>
        </div>
      </div>
      <div class="feature" role="img" aria-label="Action film poster artwork" style="background:linear-gradient(180deg,#3d3f44 0%,#6b5a4c 45%,#25272b 100%)">
        <div class="feature-caption">Title of the Movie
          <svg width="22" height="22" viewBox="0 0 22 22"><circle cx="11" cy="11" r="11" fill="rgba(255,255,255,.92)"/><path d="M9 6.5l6 4.5-6 4.5z" fill="#111317"/></svg>
        </div>
      </div>
    </section>

    <section class="card side-card">
      <div class="card-head"><span><span class="accent">Heading</span>Sub Title</span></div>
      <ul class="film-list">
        <li>
          <div class="film-thumb" role="img" aria-label="Historical film poster" style="background:linear-gradient(#b9a98a,#e6ddc8)"></div>
          <div class="film-info"><span class="film-title">Film Title</span><span class="film-meta">54,000 Views · 3 days</span><span class="film-link">Some Link <b>Movie</b></span></div>
        </li>
        <li>
          <div class="film-thumb" role="img" aria-label="Epic battle film poster" style="background:linear-gradient(#c07a2a,#4a2412)"></div>
          <div class="film-info"><span class="film-title">Film Title</span><span class="film-meta">54,000 Views · 3 days</span><span class="film-link">Some Link <b>Movie</b></span></div>
        </li>
        <li>
          <div class="film-thumb" role="img" aria-label="Animated ocean film poster" style="background:linear-gradient(#3a8fd0,#0f3f6e)"></div>
          <div class="film-info"><span class="film-title">Film Title</span><span class="film-meta">54,000 Views · 3 days</span><span class="film-link">Some Link <b>Movie</b></span></div>
        </li>
      </ul>
    </section>

    <section class="card side-card">
      <div class="card-head">Advertisement</div>
      <div class="ad-banner" role="img" aria-label="HostHarbor VPS hosting advertisement banner"></div>
    </section>
  </aside>
</main>

<footer class="site-footer">
  <div class="page footer-inner">
    <span class="company">COMPANY LOGO</span>
    <div class="link-group"><h4>Link List</h4><ul><li>Latest News</li><li>Upcoming Movies</li><li>Top Rated</li><li>New Movies</li></ul></div>
    <div class="link-group"><h4>Link List</h4><ul><li>Latest News</li><li>Upcoming Movies</li><li>Top Rated</li><li>New Movies</li></ul></div>
    <div class="legal">Copyright. All Right Reserved 2013 Movies<br>Privacy Policy · Disclaimer · Terms &amp; Condition</div>
  </div>
</footer>
</body>
</html>
```